依頼概要
■依頼の目的/概要
弊社ではあささんぽ、あさひを浴びようと思えるSNSアプリの制作を行っております。
そよかぜてちょうアプリでは毎日の記録をつけるためのライフログ系の機能を制作しております。

ライフログとして自分の記録を見返したり、他のユーザーからも見てもらえる機能がある日記のデザイン及びその画面のUI制作をお願いします。

■依頼の詳細
ユーザーが投稿するのは朝日を含めた毎朝の日記で自分のそよかぜてちょう(本のテイスト)の左ページを投稿します(アプリ上ホーム画面)。その日記投稿や朝散歩をすればするほど幸せの証として「そよかぜスター」を報酬として獲得し、毎朝獲得したハートを自分のそよかぜてちょうの右ページに貯めておけます(アプリ上そよかぜてちょう画面)。

今回トライアルでお願いしたいのはユーザーが朝日を投稿するホーム画面のUIです(左ページ)。
必要な要項といたしましては、
・ユーザーが撮影した朝日の写真(必須)
・日付(必須)
・天気※
・場所※
・気温※
・日記コメント※
・自分のキャラクター(こちらは素材があります)※

を入れられるようにしたいと考えております。
※は、ユーザー任意で入れたり、非表示にできます

スワイプすると、他のユーザーの日記のページをめくるような感覚のモーションの検討もしています。

こちらをトライアルという形で、採用された方には別画面/別バージョンの本のデザインや詳細なUIなどご相談したいと考えております。追加のUIのお見積りなども含め、ご提案いただけますと幸いです。

現在の開発中の仮デザインを添付しますが、よりよいデザインを是非、応募いただけますと幸いです。

画面UIのデザインがイメージと合っていた為。

この度、ご提案いただきありがとうございました。ご厚情にお応えすることができず、誠に申し訳ございません。勝手ではございますが、これに懲りず今後ともお付き合いくださいますようお願い申し上げます。

```html
<!DOCTYPE html>
<html lang="ja">
<head>
<meta charset="UTF-8">
<title>ホーム</title>
<link href="https://fonts.googleapis.com/css2?family=Noto+Sans+JP:wght@400;500;700&family=Roboto:wght@700&display=swap" rel="stylesheet">
<style>
  :root {
    --bg-top: #dcef86;
    --bg-bottom: #8fdcb4;
    --search-bg: #eef6d2;
    --card: #ffffff;
    --ink: #2f2f2f;
    --muted: #8a8a8a;
    --placeholder: #9a9a9a;
    --avatar: #d6d6d6;
    --fab: #ecf57a;
    --icon: #3a3a3a;
    --photo-light: #f2c45a;
    --photo-mid: #9a8a6e;
    --photo-dark: #4a4038;
  }
  * { margin: 0; padding: 0; box-sizing: border-box; }
  html, body { width: 675px; height: 1200px; overflow: hidden; }
  body {
    position: relative;
    font-family: "Noto Sans JP", sans-serif;
    background: linear-gradient(180deg, var(--bg-top) 0%, #c3e98e 40%, var(--bg-bottom) 100%);
    color: var(--ink);
  }
  .top-bar { position: absolute; top: 0; left: 0; width: 675px; height: 90px; }
  .menu-btn { position: absolute; left: 18px; top: 28px; }
  .bell-btn { position: absolute; right: 18px; top: 24px; }
  .search-field {
    position: absolute; left: 90px; top: 16px; width: 500px; height: 56px;
    background: var(--search-bg); border-radius: 6px;
    display: flex; align-items: center; padding: 0 16px;
  }
  .search-field span { flex: 1; font-size: 25px; color: var(--placeholder); }
  .next-card {
    position: absolute; left: 650px; top: 90px; width: 60px; height: 972px;
    background: var(--card); border-radius: 36px;
  }
  .diary-card {
    position: absolute; left: 4px; top: 90px; width: 633px; height: 981px;
    background: var(--card); border-radius: 36px;
  }
  .sunrise-photo {
    position: absolute; left: 25px; top: 29px; width: 581px; height: 749px;
    border-radius: 44px; overflow: hidden;
    background:
      radial-gradient(ellipse at 62% 10%, #fff1b8 0%, var(--photo-light) 16%, transparent 45%),
      linear-gradient(170deg, #b7a055 0%, var(--photo-mid) 30%, #6f6458 62%, var(--photo-dark) 100%);
  }
  .date-block {
    position: absolute; left: 40px; top: 40px; color: #fff; text-align: center;
  }
  .date-day { font-family: "Roboto", sans-serif; font-weight: 700; font-size: 66px; line-height: 1; }
  .date-month { font-family: "Roboto", sans-serif; font-weight: 700; font-size: 27px; margin-top: 6px; }
  .weather-icon { margin-top: 14px; }
  .author { position: absolute; left: 25px; top: 793px; display: flex; align-items: center; }
  .avatar { width: 72px; height: 72px; border-radius: 50%; background: var(--avatar); }
  .user-name { margin-left: 26px; font-size: 29px; }
  .diary-comment { position: absolute; left: 120px; top: 866px; font-size: 22px; letter-spacing: 0.5px; }
  .read-more {
    position: absolute; left: 0; width: 633px; top: 925px; text-align: center;
    font-size: 22px; color: var(--muted);
  }
  .bottom-nav {
    position: absolute; left: 0; top: 1102px; width: 675px; height: 98px;
    background: var(--card); display: flex; align-items: center; padding-left: 30px; gap: 36px;
  }
  .add-button {
    position: absolute; left: 546px; top: 1046px; width: 102px; height: 102px;
    border-radius: 50%; background: var(--fab);
    box-shadow: 0 3px 8px rgba(0,0,0,0.18);
    display: flex; align-items: center; justify-content: center;
  }
</style>
</head>
<body>
  <header class="top-bar">
    <svg class="menu-btn" width="36" height="30" viewBox="0 0 36 30"><g stroke="var(--icon)" stroke-width="3.5" stroke-linecap="round"><line x1="3" y1="4" x2="33" y2="4"/><line x1="3" y1="15" x2="33" y2="15"/><line x1="3" y1="26" x2="33" y2="26"/></g></svg>
    <div class="search-field">
      <span>キーワードで検索</span>
      <svg width="34" height="34" viewBox="0 0 34 34"><circle cx="14" cy="14" r="10" fill="none" stroke="var(--icon)" stroke-width="3.5"/><line x1="21.5" y1="21.5" x2="31" y2="31" stroke="var(--icon)" stroke-width="3.5" stroke-linecap="round"/></svg>
    </div>
    <svg class="bell-btn" width="36" height="40" viewBox="0 0 36 40"><path d="M6 30 V17 a12 12 0 0 1 24 0 V30 l3 3 H3 z" fill="none" stroke="var(--icon)" stroke-width="3" stroke-linejoin="round"/><path d="M14 36 a4 4 0 0 0 8 0" fill="none" stroke="var(--icon)" stroke-width="3"/></svg>
  </header>

  <div class="next-card"></div>

  <article class="diary-card">
    <div class="sunrise-photo" role="img" aria-label="朝日に照らされた小道の写真"></div>
    <div class="date-block" style="left:65px;top:120px;">
      <div class="date-day">15</div>
      <div class="date-month">Mar. 2023</div>
      <svg class="weather-icon" width="44" height="44" viewBox="0 0 44 44"><circle cx="22" cy="22" r="8" fill="none" stroke="#fff" stroke-width="3"/><g stroke="#fff" stroke-width="3" stroke-linecap="round"><line x1="22" y1="2" x2="22" y2="8"/><line x1="22" y1="36" x2="22" y2="42"/><line x1="2" y1="22" x2="8" y2="22"/><line x1="36" y1="22" x2="42" y2="22"/><line x1="8" y1="8" x2="12" y2="12"/><line x1="32" y1="32" x2="36" y2="36"/><line x1="8" y1="36" x2="12" y2="32"/><line x1="32" y1="12" x2="36" y2="8"/></g></svg>
    </div>
    <div class="author">
      <div class="avatar"></div>
      <div class="user-name">ユーザー名</div>
    </div>
    <p class="diary-comment">コメントコメントコメントコメントコメント</p>
    <p class="read-more">続きを見る</p>
  </article>

  <nav class="bottom-nav">
    <svg width="40" height="30" viewBox="0 0 40 30"><g stroke="var(--icon)" stroke-width="3.5" stroke-linecap="round"><line x1="4" y1="4" x2="36" y2="4"/><line x1="4" y1="15" x2="36" y2="15"/><line x1="4" y1="26" x2="36" y2="26"/></g></svg>
    <svg width="42" height="42" viewBox="0 0 42 42"><path d="M5 19 L21 5 L37 19 V38 H26 V26 H16 V38 H5 Z" fill="none" stroke="var(--icon)" stroke-width="3" stroke-linejoin="round"/></svg>
    <svg width="42" height="42" viewBox="0 0 42 42"><circle cx="21" cy="13" r="8" fill="none" stroke="var(--icon)" stroke-width="3"/><path d="M5 38 a16 12 0 0 1 32 0 Z" fill="none" stroke="var(--icon)" stroke-width="3" stroke-linejoin="round"/></svg>
    <svg width="42" height="40" viewBox="0 0 42 40"><path d="M21 36 L6 21 a9 9 0 0 1 15 -12 a9 9 0 0 1 15 12 Z" fill="none" stroke="var(--icon)" stroke-width="3" stroke-linejoin="round"/></svg>
  </nav>

  <div class="add-button">
    <svg width="34" height="34" viewBox="0 0 34 34"><g stroke="var(--icon)" stroke-width="3.5" stroke-linecap="round"><line x1="17" y1="3" x2="17" y2="31"/><line x1="3" y1="17" x2="31" y2="17"/></g></svg>
  </div>
</body>
</html>
```